New Design for our Velintor Gran Reserva Brandy, it is the label design for the bottle label

We need a new bottle label for our Brandy Gran Reserva that we want to bring to the market.

Please have a look at all our current bottles and labels and the feel of our company under www.velintor-example.ch

The bottle that we will be using for the brand is a different one than the one that we already have, the design of the bottle is attached with a document.

I have also attached a briefing in regards to Brandy in general for your information.

### 1. What is Brandy?
Brandy is a distilled spirit made from fermented wine or other fruit wines. It is traditionally aged in oak barrels, which gives it its characteristic color and rich flavor. The aging process in oak is essential for developing the aromas and quality of the brandy.

### 2. What is Brandy Reserva?
A Brandy labeled as "Reserva" has undergone a longer aging process, typically at least 2 to 3 years, in oak barrels. This aging gives the brandy a deeper, more complex flavor profile and a darker color. "Reserva" is often an indication of higher quality.

### 3. Who enjoys drinking Brandy?
Brandy is typically favored by those who appreciate a deep, rich tasting experience. This often includes older consumers who value the time-aged complexity of the spirit. However, Brandy is also gaining popularity among younger people, especially through cocktails and modern serving styles.

### 4. Why is Brandy trending?
Brandy is experiencing a resurgence as consumers increasingly value quality and artisanal production methods. Its versatility in cocktails and association with traditional, luxurious experiences have also contributed to its renewed popularity.

### 5. What colors would be associated with Brandy?
The typical colors associated with Brandy are warm gold, amber, and deep golden-brown tones. These colors reflect the aging process in oak barrels and the richness of the flavors. Other associated colors might include dark brown and mahogany.

### 6. What is important to customers when buying Brandy?
Customers care about the origin of the Brandy, the aging time, the quality of the ingredients, the production method, and the brand. They also pay attention to the prestige of the product and the authenticity of the production.

### 7. What is not important to customers when buying Brandy?
For many customers, the price and packaging (unless it’s especially exclusive) may be less important than the quality and taste of the Brandy. The distillery name might be less significant if it isn’t tied to a particular reputation.

### 8. What do customers know about Swiss Brandy?
Swiss Brandy is still relatively unknown in many markets, but customers who are familiar with it appreciate the precision and quality of Swiss production. Swiss Brandy is assumed to be made with care and under strict quality standards.

### 9. What is Brandy Gran Reserva?
**Brandy Gran Reserva** is an even higher quality and longer-aged version of Brandy. Generally, a Gran Reserva is aged for at least 5 to 10 years or more in oak barrels. This extended aging process gives the Brandy an especially deep, complex flavor profile and often a darker, richer color. Gran Reserva is often regarded as the top-tier product within a Brandy range and appeals to discerning consumers who value quality, refinement, and a luxurious tasting experience.

The label “Gran Reserva” thus indicates the highest quality level for Brandies, similar to other spirits (like wine or whisky), where the aging time is a critical factor.

### 10. What emotions are associated with Brandy?
Brandy is often associated with luxury, relaxation, and comfort. It evokes feelings of tradition, elegance, and sophistication. Drinking Brandy is frequently seen as a moment of reflection and enjoyment.

### 11. How should Brandy be marketed?
Brandy should be marketed with a focus on its artisanal production, quality, and tradition. A narrative around the product, its aging, and origin can help create an emotional connection with the customer. The marketing should also emphasize the versatility of Brandy, whether consumed neat or in cocktails.

### 12. Sales test and label design for Velintor Brandy
For a sales test, I would suggest a tasting in an upscale setting, perhaps paired with a storytelling presentation highlighting the history of the 6-year aged Brandy and its aging in oak barrels.

**Label design**:
The label should reflect the exclusivity of the product, with an elegant, minimalist design. Colors like deep gold, mahogany, and a hint of deep blue could be used to emphasize the aging and quality of the Brandy. The label should include information about the aging time, the use of oak barrels, and a brief story about the Brandy’s production. A seal or embossing highlighting the craftsmanship would also be fitting.

Target Market(s)

Customers that like Brandy

Requirements
Must have
• the Alcohol % must be included on the label as well as our address.

```html
<!DOCTYPE html>
<html lang="en">
<head>
<meta charset="utf-8">
<title>Velintor Gran Reserva Brandy – Bottle Label</title>
<link rel="stylesheet" href="https://fonts.googleapis.com/css2?family=Roboto+Slab:wght@400;600;700&family=Rye&display=swap">
<style>
  :root {
    --page-bg: #f4f1ec;
    --gold-light: #f3d27a;
    --gold-mid: #c9923b;
    --gold-dark: #8a5a1e;
    --red-main: #961b29;
    --red-light: #a41e2d;
    --red-dark: #640e18;
    --red-deep: #520a13;
    --wood-light: #c87a3a;
    --wood-mid: #8c4a1c;
    --wood-dark: #3b1f0e;
    --navy-band: #0f1c26;
    --barrel-light: #7a5638;
    --barrel-dark: #2e1d12;
    --ink-white: #ffffff;
    --ink-cream: #f6eee2;
  }
  html, body {
    margin: 0;
    padding: 0;
    width: 1200px;
    height: 883px;
    overflow: hidden;
    background: var(--page-bg);
  }
  .canvas {
    width: 1200px;
    height: 883px;
    display: flex;
    align-items: center;
    justify-content: center;
  }
  .label {
    width: 400px;
    height: 818px;
    display: block;
    filter: drop-shadow(0 6px 14px rgba(0,0,0,0.22));
  }
  .brand-name {
    font-family: "Roboto Slab", serif;
    font-weight: 700;
    font-size: 36px;
    fill: var(--ink-white);
  }
  .brand-sub {
    font-family: "Roboto Slab", serif;
    font-weight: 600;
    font-size: 15px;
    letter-spacing: 1px;
    fill: var(--ink-white);
  }
  .title-display {
    font-family: "Rye", serif;
    fill: var(--ink-cream);
  }
  .title-shadow {
    font-family: "Rye", serif;
    fill: var(--red-deep);
  }
  .title-kind {
    font-family: "Roboto Slab", serif;
    font-weight: 700;
    font-size: 29px;
    fill: var(--ink-cream);
  }
  .aging-note {
    font-family: "Roboto Slab", serif;
    font-weight: 600;
    font-size: 14px;
    fill: var(--ink-white);
  }
  .spec {
    font-family: "Roboto Slab", serif;
    font-weight: 700;
    font-size: 17px;
    fill: var(--ink-white);
  }
</style>
</head>
<body>
<main class="canvas">
  <svg class="label" viewBox="0 0 502 1027" xmlns="http://www.w3.org/2000/svg" aria-label="Velintor Gran Reserva Brandy label">
    <defs>
      <linearGradient id="gold-frame" x1="0" y1="0" x2="1" y2="1">
        <stop offset="0" stop-color="var(--gold-dark)"/>
        <stop offset="0.3" stop-color="var(--gold-light)"/>
        <stop offset="0.55" stop-color="var(--gold-mid)"/>
        <stop offset="0.8" stop-color="var(--gold-light)"/>
        <stop offset="1" stop-color="var(--gold-dark)"/>
      </linearGradient>
      <linearGradient id="wood-tone" x1="0" y1="0" x2="1" y2="1">
        <stop offset="0" stop-color="var(--wood-dark)"/>
        <stop offset="0.4" stop-color="var(--wood-light)"/>
        <stop offset="0.75" stop-color="var(--wood-mid)"/>
        <stop offset="1" stop-color="var(--wood-dark)"/>
      </linearGradient>
      <radialGradient id="barrel-tone" cx="0.55" cy="0.5" r="0.6">
        <stop offset="0" stop-color="var(--barrel-light)"/>
        <stop offset="1" stop-color="var(--barrel-dark)"/>
      </radialGradient>
      <clipPath id="label-body">
        <polygon points="251,18 484,98 446,1012 56,1012 18,98"/>
      </clipPath>
    </defs>

    <!-- gold frame -->
    <polygon class="label-frame" points="251,0 502,85 442,1027 60,1027 0,85" fill="url(#gold-frame)"/>

    <!-- red body with facets -->
    <g class="label-body" clip-path="url(#label-body)">
      <rect x="0" y="0" width="502" height="1027" fill="var(--red-main)"/>
      <!-- header facets -->
      <polygon points="251,18 0,100 0,197 90,197" fill="var(--red-dark)"/>
      <polygon points="251,18 502,98 502,197 470,197" fill="var(--red-dark)"/>
      <polygon points="251,18 330,197 470,197" fill="var(--red-light)"/>
      <!-- lower facets -->
      <polygon points="110,530 300,760 466,530" fill="var(--red-dark)" opacity="0.55"/>
      <polygon points="340,530 502,530 502,700" fill="var(--red-deep)"/>
      <polygon points="0,760 260,720 502,690 502,1012 0,1012" fill="var(--red-light)"/>
      <polygon points="0,945 502,945 502,1027 0,1027" fill="var(--red-dark)"/>
      <polygon points="40,945 251,1012 460,945" fill="var(--red-main)"/>
    </g>

    <!-- brand mark -->
    <g class="brand">
      <text class="brand-name" x="251" y="124" text-anchor="middle">Velintor</text>
      <text class="brand-sub" x="247" y="142" text-anchor="middle">SWISS</text>
      <text class="brand-sub" x="247" y="159" text-anchor="middle">DISTILLERY</text>
    </g>

    <!-- title panel -->
    <line x1="24" y1="198" x2="480" y2="198" stroke="url(#gold-frame)" stroke-width="3"/>
    <rect class="wood-panel" x="24" y="200" width="456" height="297" fill="url(#wood-tone)" role="img" aria-label="Weathered oak wood texture"/>
    <g class="title">
      <text class="title-shadow" x="64" y="322" font-size="92" textLength="226" lengthAdjust="spacingAndGlyphs">GRAN</text>
      <text class="title-display" x="60" y="317" font-size="92" textLength="226" lengthAdjust="spacingAndGlyphs">GRAN</text>
      <text class="title-shadow" x="142" y="397" font-size="88" textLength="306" lengthAdjust="spacingAndGlyphs">RESERVA</text>
      <text class="title-display" x="138" y="392" font-size="88" textLength="306" lengthAdjust="spacingAndGlyphs">RESERVA</text>
      <text class="title-kind" x="252" y="428" textLength="142" lengthAdjust="spacingAndGlyphs">BRANDY</text>
    </g>

    <!-- aging band -->
    <rect x="34" y="497" width="426" height="33" fill="var(--navy-band)"/>
    <line x1="34" y1="531" x2="460" y2="531" stroke="url(#gold-frame)" stroke-width="2"/>
    <text class="aging-note" x="247" y="519" text-anchor="middle">AGED FOR 6 YEARS IN OAK BARRELS</text>

    <!-- barrels -->
    <rect class="barrel-art" x="152" y="822" width="205" height="140" rx="30" fill="url(#barrel-tone)" role="img" aria-label="Two oak barrels, one upright and one lying on its side"/>

    <!-- specs -->
    <text class="spec" x="90" y="970">alc 40%</text>
    <text class="spec" x="357" y="970">0.5 l</text>
  </svg>
</main>
</body>
</html>
```